Harbor LunaVital & Equipments

I need to create full stationery design for the company; Business Card, Envelop, Letterheads, Calendar and email template.

Our company is specialized in the import and export of nutritional, pharmaceutical and cosmetics in addition to medical equipments.

These is no limitation on how to use colors within the design.

Target Market(s)

Global

Industry/Entity Type

Healthcare

Other font styles liked:
• a font close to logo. Letterhead body text to be different than the address text

Requirements
Nice to have
• We will have multiple locations so it is good to keep space for future addresses.
• Stationary requirements:
• Letterhead: A4
• Envelopes: 3 regular sizes : large, medium and small (i do not know the sizes)
• Colors: extracted from the logo

```html
<!DOCTYPE html>
<html lang="en">
<head>
<meta charset="utf-8">
<title>Harbor LunaVital &amp; Equipments — Business Card</title>
<link rel="stylesheet" href="https://fonts.googleapis.com/css2?family=Nunito:wght@700;800&family=Arimo:wght@400;700&display=swap">
<style>
  :root {
    --page: #ecebe7;
    --white: #ffffff;
    --brand-blue: #27a3dd;
    --brand-blue-deep: #1b8fcf;
    --brand-green: #2f9a2c;
    --brand-green-dark: #1f7a1e;
    --brand-green-light: #3aac37;
    --navy: #1d2a78;
    --text-light: #ffffff;
  }
  * { box-sizing: border-box; margin: 0; padding: 0; }
  html, body { width: 1200px; height: 950px; overflow: hidden; }
  body {
    background: var(--page);
    font-family: "Arimo", Arial, sans-serif;
    position: relative;
  }
  .card {
    position: absolute;
    left: 290px;
    width: 620px;
    height: 354px;
    border-radius: 22px;
    overflow: hidden;
    box-shadow: 0 10px 28px rgba(0,0,0,0.18);
  }
  /* Back side */
  .card--back {
    top: 70px;
    background: linear-gradient(135deg, var(--brand-green-light) 0%, var(--brand-green) 55%, var(--brand-green-dark) 100%);
    display: flex;
    flex-direction: column;
    align-items: center;
    justify-content: center;
    gap: 18px;
  }
  .back-mark {
    display: flex;
    align-items: center;
    gap: 16px;
  }
  .back-mark__square {
    width: 64px; height: 64px;
    background: rgba(255,255,255,0.9);
    border-radius: 8px;
  }
  .back-mark__name {
    font-family: "Nunito", Arial, sans-serif;
    font-weight: 800;
    font-size: 30px;
    line-height: 1.15;
    color: var(--text-light);
  }
  .back-web {
    font-size: 15px;
    letter-spacing: 4px;
    color: rgba(255,255,255,0.8);
  }
  /* Front side */
  .card--front {
    top: 526px;
    background: var(--white);
  }
  .front-waves {
    position: absolute;
    inset: 0;
    width: 100%;
    height: 100%;
  }
  .brand {
    position: absolute;
    left: 44px;
    top: 70px;
    display: flex;
    align-items: center;
    gap: 14px;
  }
  .brand__square {
    width: 44px; height: 44px;
    background: var(--navy);
    border-radius: 5px;
  }
  .brand__name {
    font-family: "Nunito", Arial, sans-serif;
    font-weight: 800;
    font-size: 26px;
    line-height: 1.1;
    color: var(--brand-blue);
    width: 250px;
  }
  .person {
    position: absolute;
    right: 40px;
    top: 120px;
    text-align: right;
    font-family: "Arimo", Arial, sans-serif;
    font-weight: 700;
  }
  .person__name { font-size: 19px; color: var(--brand-blue-deep); }
  .person__role { font-size: 16px; color: var(--brand-green); margin-top: 2px; }
  .contacts {
    position: absolute;
    right: 36px;
    top: 236px;
    list-style: none;
    color: var(--text-light);
    font-size: 14px;
    line-height: 19px;
  }
  .contacts li {
    display: flex;
    justify-content: flex-end;
    align-items: center;
    gap: 10px;
  }
  .contacts svg { width: 14px; height: 14px; fill: var(--text-light); flex: none; }
  .address {
    position: absolute;
    left: 150px;
    bottom: 22px;
    color: var(--text-light);
    font-size: 14px;
  }
</style>
</head>
<body>

  <section class="card card--back" aria-label="Business card, back">
    <div class="back-mark">
      <span class="back-mark__square"></span>
      <span class="back-mark__name">Harbor LunaVital</span>
    </div>
    <p class="back-web">www.harborluna.com</p>
  </section>

  <section class="card card--front" aria-label="Business card, front">
    <svg class="front-waves" viewBox="0 0 620 354" preserveAspectRatio="none" aria-hidden="true">
      <path d="M0 170 C 120 180, 220 210, 330 218 C 420 224, 520 212, 620 196" fill="none" stroke="var(--brand-green)" stroke-width="7"/>
      <path d="M0 192 C 140 200, 240 232, 350 234 C 450 236, 540 216, 620 200 L620 354 L0 354 Z" fill="var(--brand-blue)"/>
      <path d="M0 186 C 140 196, 240 226, 350 228 C 450 230, 540 212, 620 196" fill="none" stroke="var(--white)" stroke-width="4"/>
    </svg>

    <div class="brand">
      <span class="brand__square"></span>
      <span class="brand__name">Harbor LunaVital &amp; Equipments</span>
    </div>

    <div class="person">
      <p class="person__name">Marcus Hale</p>
      <p class="person__role">President</p>
    </div>

    <ul class="contacts">
      <li>412 5590 1876
        <svg viewBox="0 0 24 24"><path d="M6.6 10.8a15 15 0 0 0 6.6 6.6l2.2-2.2a1 1 0 0 1 1-.25 11.4 11.4 0 0 0 3.6.57 1 1 0 0 1 1 1V20a1 1 0 0 1-1 1A17 17 0 0 1 3 4a1 1 0 0 1 1-1h3.5a1 1 0 0 1 1 1c0 1.25.2 2.45.57 3.57a1 1 0 0 1-.25 1z"/></svg>
      </li>
      <li>318 7742 6093
        <svg viewBox="0 0 24 24"><path d="M7 2h10a2 2 0 0 1 2 2v16a2 2 0 0 1-2 2H7a2 2 0 0 1-2-2V4a2 2 0 0 1 2-2zm0 3v12h10V5zm5 13.5a1 1 0 1 0 0 2 1 1 0 0 0 0-2z"/></svg>
      </li>
      <li>marcus@harborluna.com
        <svg viewBox="0 0 24 24"><path d="M3 5h18a1 1 0 0 1 1 1v12a1 1 0 0 1-1 1H3a1 1 0 0 1-1-1V6a1 1 0 0 1 1-1zm1 2.3V17h16V7.3l-8 5.2z"/></svg>
      </li>
      <li>www.harborluna.com
        <svg viewBox="0 0 24 24"><path d="M12 2a10 10 0 1 0 0 20 10 10 0 0 0 0-20zm0 2c.9 1.2 1.6 2.6 2 4h-4c.4-1.4 1.1-2.8 2-4zM4.3 14a8 8 0 0 1 0-4h3.4a16 16 0 0 0 0 4zm5.4 0a14 14 0 0 1 0-4h4.6a14 14 0 0 1 0 4zm6.6 0a16 16 0 0 0 0-4h3.4a8 8 0 0 1 0 4z"/></svg>
      </li>
    </ul>

    <p class="address">2291 Willow Crest Road, Juneau, Alaska 99801</p>
  </section>

</body>
</html>
```